Business cards

I would like a black background with the design I previously chose. I need 2 sets of cards. Mine will have Rebecca Halvorsen, Broker/Owner, 307-418-2736 and rebecca.pinecrestrealty@mailvane.com
The second set will read, Dana Wexford, Realtor 307-582-4069, dana.pinecrestrealty@mailvane.com

```html
<!DOCTYPE html>
<html lang="en">
<head>
<meta charset="utf-8">
<title>Pinecrest Realty Group – Business Cards</title>
<link href="https://fonts.googleapis.com/css2?family=Marcellus&family=Josefin+Sans:wght@300;400&display=swap" rel="stylesheet">
<style>
  :root {
    --page: #ffffff;
    --card: #000000;
    --taupe: #8c8475;
    --taupe-dark: #5f5a50;
    --steel: #8f9cab;
    --steel-line: #5d6b7a;
    --white: #ffffff;
  }
  html, body {
    margin: 0;
    width: 1200px;
    height: 1200px;
    overflow: hidden;
    background: var(--page);
  }
  .sheet { position: relative; width: 1200px; height: 1200px; }
  .card {
    position: absolute;
    width: 470px;
    height: 280px;
    background: var(--card);
    overflow: hidden;
  }
  .card--a { left: 121px; }
  .card--b { left: 609px; }
  .row-stone .card { top: 303px; }
  .row-steel .card { top: 617px; }

  .brand { position: absolute; left: 20px; top: 20px; width: 150px; text-align: center; }
  .brand__dot {
    width: 60px; height: 60px; border-radius: 50%;
    margin: 0 auto 6px;
  }
  .brand__name {
    font-family: "Marcellus", serif;
    font-size: 14px;
    letter-spacing: 0.5px;
    white-space: nowrap;
  }

  .person { position: absolute; left: 220px; top: 60px; width: 200px; text-align: center; }
  .person__name {
    font-family: "Marcellus", serif;
    font-size: 17px;
    letter-spacing: 0.3px;
    text-transform: uppercase;
    white-space: nowrap;
  }
  .person__title {
    font-family: "Josefin Sans", sans-serif;
    font-size: 11px;
    letter-spacing: 2.2px;
    margin-top: 1px;
  }

  .contact { position: absolute; left: 221px; top: 173px; font-family: "Josefin Sans", sans-serif; font-weight: 300; font-size: 12px; }
  .contact__line { display: flex; align-items: center; height: 15px; white-space: nowrap; }
  .contact__icon { width: 13px; height: 13px; margin-right: 8px; flex: none; }

  .stone-band {
    position: absolute; left: 0; right: 0; top: 242px; height: 16px;
    background: linear-gradient(to bottom, #a49c8c 0, #6f6a60 3px, #8a8375 6px, #3a3834 8px, #1a1918 12px, #000 16px);
  }
  .steel-band {
    position: absolute; left: 0; right: 0; top: 243px; height: 4px;
    background: var(--steel-line);
  }

  .theme-stone { color: var(--taupe); }
  .theme-stone .brand__dot { background: var(--taupe-dark); }
  .theme-stone .icon-fill { fill: var(--taupe); }
  .theme-steel { color: var(--white); }
  .theme-steel .brand__name { color: var(--steel); }
  .theme-steel .brand__dot { background: var(--steel); }
  .theme-steel .icon-fill { fill: var(--white); }
</style>
</head>
<body>
<svg width="0" height="0" style="position:absolute">
  <defs>
    <symbol id="icon-phone" viewBox="0 0 13 13">
      <rect class="icon-fill" x="0" y="0" width="13" height="13" rx="3"/>
      <rect x="3.5" y="2.5" width="6" height="8" rx="1" fill="#000"/>
      <rect class="icon-fill" x="4.5" y="3.5" width="4" height="5.5"/>
    </symbol>
    <symbol id="icon-globe" viewBox="0 0 13 13">
      <rect class="icon-fill" x="0" y="0" width="13" height="13" rx="3"/>
      <circle cx="6.5" cy="6.5" r="4" fill="#000"/>
      <path class="icon-fill" d="M4 5.5 q1.5 -1 2.5 0 q0 1.5 -1.5 2 z M7.5 7 q1.5 0 2 1.5 q-1 1 -2 0.5 z"/>
    </symbol>
  </defs>
</svg>

<main class="sheet">
  <section class="row-stone">
    <article class="card card--a theme-stone">
      <div class="brand"><div class="brand__dot"></div><div class="brand__name">PINECREST REALTY</div></div>
      <div class="person"><div class="person__name">Rebecca Halvorsen</div><div class="person__title">Broker/Owner</div></div>
      <div class="contact">
        <div class="contact__line"><svg class="contact__icon"><use href="#icon-phone"/></svg>307-418-2736</div>
        <div class="contact__line"><svg class="contact__icon"><use href="#icon-globe"/></svg>rebecca.pinecrestrealty@mailvane.com</div>
      </div>
      <div class="stone-band" role="img" aria-label="Textured stone strip"></div>
    </article>
    <article class="card card--b theme-stone">
      <div class="brand"><div class="brand__dot"></div><div class="brand__name">PINECREST REALTY</div></div>
      <div class="person"><div class="person__name">Dana Wexford</div><div class="person__title">Realtor</div></div>
      <div class="contact">
        <div class="contact__line"><svg class="contact__icon"><use href="#icon-phone"/></svg>307-582-4069,</div>
        <div class="contact__line"><svg class="contact__icon"><use href="#icon-globe"/></svg>dana.pinecrestrealty@mailvane.com</div>
      </div>
      <div class="stone-band" role="img" aria-label="Textured stone strip"></div>
    </article>
  </section>

  <section class="row-steel">
    <article class="card card--a theme-steel">
      <div class="brand"><div class="brand__dot"></div><div class="brand__name">PINECREST REALTY</div></div>
      <div class="person"><div class="person__name">Rebecca Halvorsen</div><div class="person__title">Broker/Owner</div></div>
      <div class="contact">
        <div class="contact__line"><svg class="contact__icon"><use href="#icon-phone"/></svg>307-418-2736</div>
        <div class="contact__line"><svg class="contact__icon"><use href="#icon-globe"/></svg>rebecca.pinecrestrealty@mailvane.com</div>
      </div>
      <div class="steel-band"></div>
    </article>
    <article class="card card--b theme-steel">
      <div class="brand"><div class="brand__dot"></div><div class="brand__name">PINECREST REALTY</div></div>
      <div class="person"><div class="person__name">Dana Wexford</div><div class="person__title">Realtor</div></div>
      <div class="contact">
        <div class="contact__line"><svg class="contact__icon"><use href="#icon-phone"/></svg>307-582-4069,</div>
        <div class="contact__line"><svg class="contact__icon"><use href="#icon-globe"/></svg>dana.pinecrestrealty@mailvane.com</div>
      </div>
      <div class="steel-band"></div>
    </article>
  </section>
</main>
</body>
</html>
```